Brightmere Facebook Design

Build out a really nice and professional Facebook Page and full banner for Brightmere perhaps with the our services portfolio across the page as well,
Pls check www.brightmere-example.com.au for ideas to a make the Facebook Page look professional like a similar theme to our website and the porfolio of services

Main photo please emphasis the equipment cleaning and the gurney cleaning a lower priority to emphasize is the general cleaning
Thanks very much

Target Market(s)

Restaurant, warehouses, factories, car and fleet companies, hotels and buffets, chain restaurants, pizza huts, burger eateries, leisure centres

Industry/Entity Type

Cleaning Services

Font styles to use
Serif

Colors
3277b5
f04a50
f37122
fcf299
ec1f27

Requirements
Must have
• Energy and professional Facebook Site with some of the Brightmere Flowers across it and the portfolio of services
Nice to have
• Good vibrant colours

Professional similar to the website

```html
<!DOCTYPE html>
<html lang="en">
<head>
<meta charset="utf-8">
<title>Brightmere – Facebook Cover</title>
<link rel="stylesheet" href="https://fonts.googleapis.com/css2?family=Roboto:wght@300;500;700&family=Tinos:wght@400;700&display=swap">
<style>
  :root {
    --navy: #1d4f8f;
    --blue: #3277b5;
    --orange: #f37122;
    --red: #ec1f27;
    --coral: #f04a50;
    --white: #ffffff;
    --banner-dark: rgba(40, 12, 6, 0.88);
  }
  * { box-sizing: border-box; margin: 0; padding: 0; }
  html, body { width: 1200px; height: 527px; overflow: hidden; background: var(--white); }

  .cover {
    position: relative;
    width: 1200px;
    height: 527px;
    overflow: hidden;
    font-family: "Tinos", "Times New Roman", serif;
  }

  .photo { position: absolute; top: 0; left: 0; width: 100%; height: 100%; }
  .photo--kitchen {
    background: radial-gradient(ellipse at 30% 35%, #c4562a 0%, #8a3418 35%, #3e1a10 75%, #2a130c 100%);
  }
  .photo--gurney {
    clip-path: polygon(715px 0, 1200px 0, 1200px 527px, 540px 527px);
    background: linear-gradient(160deg, #4f6474 0%, #344553 45%, #1f2c37 100%);
  }

  .headline {
    position: absolute;
    left: 271px; top: 154px;
    width: 651px; height: 87px;
    display: flex;
    border: 1px solid rgba(255,255,255,0.75);
    font-family: "Roboto", Arial, sans-serif;
    color: var(--white);
    background: linear-gradient(90deg, #6e1608 0%, #a22410 45%, var(--banner-dark) 62%, rgba(30,14,10,0.9) 100%);
  }
  .headline__item {
    display: flex; flex-direction: column; justify-content: center;
    line-height: 1.12;
    white-space: nowrap;
  }
  .headline__item--equipment { padding-left: 24px; width: 350px; }
  .headline__item--gurney { padding-left: 28px; }
  .headline__light { font-weight: 300; font-size: 22px; letter-spacing: 0.3px; }
  .headline__bold { font-weight: 700; font-size: 26px; letter-spacing: 0.5px; }
  .headline__slash {
    position: absolute; left: 350px; top: 10px;
    width: 2px; height: 67px; background: var(--white);
    transform: skewX(-18deg);
  }

  .base { position: absolute; left: 0; top: 0; }

  .service-card {
    position: absolute;
    width: 117px; height: 74px;
    background: var(--white);
    border-radius: 7px;
    box-shadow: 0 3px 6px rgba(0,0,0,0.35);
    display: flex; flex-direction: column; align-items: center; justify-content: center;
    text-align: center;
    padding: 4px 2px;
  }
  .service-card__name {
    color: var(--navy);
    font-size: 10px;
    line-height: 1.1;
    letter-spacing: -0.2px;
    white-space: nowrap;
    margin-bottom: 7px;
  }
  .service-card__type {
    color: var(--orange);
    font-weight: 700;
    font-size: 13px;
    letter-spacing: 0.2px;
    white-space: nowrap;
  }
  .service-card__type--red { color: var(--red); }

  .brand {
    position: absolute;
    left: 0; width: 100%; top: 418px;
    text-align: center;
  }
  .brand__name {
    font-family: "Roboto", Arial, sans-serif;
    font-size: 30px; font-weight: 500; color: var(--navy);
    letter-spacing: 1px;
  }
</style>
</head>
<body>
<div class="cover">
  <div class="photo photo--kitchen" role="img" aria-label="Commercial kitchen with a soft-serve machine and food trays"></div>
  <div class="photo photo--gurney" role="img" aria-label="High pressure gurney spraying water over paving"></div>

  <div class="headline">
    <div class="headline__item headline__item--equipment">
      <span class="headline__light">EQUIPMENT CLEANING AND</span>
      <span class="headline__bold">SANITISATION SERVICE</span>
    </div>
    <span class="headline__slash"></span>
    <div class="headline__item headline__item--gurney">
      <span class="headline__light">HIGH PRESSURE</span>
      <span class="headline__bold">GURNEY&nbsp; CLEANING</span>
    </div>
  </div>

  <svg class="base" width="1200" height="527" viewBox="0 0 1200 527" aria-hidden="true">
    <path d="M0 360 Q300 330 600 350 L600 527 L0 527 Z" fill="var(--orange)"/>
    <path d="M1200 330 Q900 340 600 350 L600 527 L1200 527 Z" fill="var(--navy)"/>
    <path d="M0 385 Q300 360 600 378 Q900 360 1200 360 L1200 527 L0 527 Z" fill="var(--white)"/>
  </svg>

  <div class="service-card" style="left:102px; top:366px;">
    <p class="service-card__name">Kitchen<br>Detail Cleaning</p>
    <p class="service-card__type">SERVICE</p>
  </div>
  <div class="service-card" style="left:227px; top:337px;">
    <p class="service-card__name">General Cleaning &amp;<br>Property Facilities</p>
    <p class="service-card__type service-card__type--red">MANAGEMENT</p>
  </div>
  <div class="service-card" style="left:351px; top:310px;">
    <p class="service-card__name">High pressure gurney &amp;<br>play ground equipment</p>
    <p class="service-card__type">CLEANING</p>
  </div>
  <div class="service-card" style="left:480px; top:300px;">
    <p class="service-card__name">Projects and<br>Recruiting Services</p>
    <p class="service-card__type service-card__type--red">WORK WITH US</p>
  </div>
  <div class="service-card" style="left:604px; top:300px;">
    <p class="service-card__name">Equipment Cleaning &amp;<br>Sanitisation</p>
    <p class="service-card__type">SERVICE</p>
  </div>
  <div class="service-card" style="left:729px; top:310px;">
    <p class="service-card__name">Kitchen<br>Detail Cleaning</p>
    <p class="service-card__type">SERVICE</p>
  </div>
  <div class="service-card" style="left:853px; top:337px;">
    <p class="service-card__name">General Cleaning &amp;<br>Property Facilities</p>
    <p class="service-card__type service-card__type--red">MANAGEMENT</p>
  </div>
  <div class="service-card" style="left:977px; top:366px;">
    <p class="service-card__name">High pressure gurney &amp;<br>play ground equipment</p>
    <p class="service-card__type">CLEANING</p>
  </div>

  <div class="brand">
    <span class="brand__name">Brightmere</span>
  </div>
</div>
</body>
</html>
```